Powerpoint Slide Deck

I had my logo designed using drafthollow and would like to have a professional looking powerpoint deck created with my logo etc. my website is vantreo.info

```html
<!DOCTYPE html>
<html lang="en">
<head>
<meta charset="utf-8">
<title>Vantreo – Presentation Template</title>
<link href="https://fonts.googleapis.com/css2?family=Montserrat:wght@500;600;700&family=Open+Sans:wght@400;600;700&display=swap" rel="stylesheet">
<style>
:root{
  --bg:#e8e9eb;
  --ink:#1e1f21;
  --blue:#2a8fd6;
  --green:#4cb848;
  --violet:#6245a6;
  --magenta:#9a2b8e;
  --slate:#5d5e60;
  --muted:#8a8c8f;
  --line:#c9cbce;
  --white:#ffffff;
  --photo-dark:linear-gradient(135deg,#15293d 0%,#2c5275 55%,#5d86a8 100%);
  --photo-light:linear-gradient(135deg,#c9d3dc 0%,#e6ebef 60%,#d3dae1 100%);
}
*{box-sizing:border-box;margin:0;padding:0}
html,body{width:1200px;height:2913px;overflow:hidden;background:var(--bg)}
body{position:relative;font-family:"Open Sans",Arial,sans-serif;color:var(--ink)}

.brand-hero{position:absolute;left:0;width:1200px;top:168px;text-align:center;font-family:"Montserrat",Arial,sans-serif;font-weight:600;font-size:64px;color:var(--ink);letter-spacing:1px}
.tagline{position:absolute;left:0;width:1200px;top:286px;text-align:center;font-size:17px;letter-spacing:.4px;color:var(--ink)}
.feature{position:absolute;top:336px;width:92px;height:60px;display:flex;align-items:center;justify-content:center;text-align:center;color:var(--white);font-size:14px;line-height:17px}
.feature.blue{background:var(--blue)} .feature.green{background:var(--green)} .feature.violet{background:var(--violet)} .feature.magenta{background:var(--magenta)} .feature.slate{background:var(--slate)}

.slide{position:absolute;background:var(--white);overflow:hidden}
.strip{position:absolute;left:0;right:0;bottom:0;height:4px;background:linear-gradient(90deg,var(--ink) 0 52%,var(--blue) 52% 68%,var(--green) 68% 84%,var(--magenta) 84% 100%)}
.photo{position:absolute;background:var(--photo-dark)}
.photo.round{border-radius:50%}
.title{position:absolute;left:15px;top:13px;font-weight:600;font-size:10px;color:var(--ink)}
.subtitle{position:absolute;left:15px;top:26px;font-size:5px;color:var(--muted)}
.mini-brand{position:absolute;right:12px;top:12px;font-family:"Montserrat",Arial,sans-serif;font-weight:600;font-size:7px;color:var(--ink)}
.foot{position:absolute;left:12px;bottom:8px;font-size:4px;color:var(--muted)}
.page{position:absolute;right:12px;bottom:8px;font-size:4px;color:var(--muted)}
.tiny{font-size:5px;line-height:7px;color:var(--slate)}
.abs{position:absolute}
.wordmark{font-family:"Montserrat",Arial,sans-serif;font-weight:600;color:var(--ink)}
.headline{font-family:"Montserrat",Arial,sans-serif;font-weight:700;color:var(--magenta);text-transform:uppercase}
.url{font-size:10px;letter-spacing:2.4px;color:var(--blue)}
svg{position:absolute;overflow:visible}
.g{color:var(--green)} .b{color:var(--blue)} .v{color:var(--violet)} .m{color:var(--magenta)}

.agenda-num{position:absolute;width:18px;height:18px;color:var(--white);font-size:10px;font-weight:600;display:flex;align-items:center;justify-content:center}
.agenda-label{position:absolute;font-size:11px;color:var(--ink)}
.agenda-desc{position:absolute;width:118px;font-size:5.5px;line-height:8px;color:var(--muted)}

.plan{position:absolute;top:41px;width:68px;height:55px;color:var(--white);text-align:center}
.plan .name{font-size:7px;font-weight:600;margin-top:8px}
.plan .price{font-family:"Montserrat",Arial,sans-serif;font-weight:700;font-size:22px;line-height:26px;margin-top:4px}
.plan .price sup{font-size:8px;vertical-align:top;margin-right:2px}
.plan-body{position:absolute;top:96px;width:68px;height:62px;background:#f1f2f3;padding:6px 5px}
.plan-body p{font-size:4px;line-height:7px;color:var(--muted);border-bottom:1px solid #dfe0e2}

.badge{position:absolute;height:8px;background:var(--blue);color:var(--white);font-size:4.5px;font-weight:700;display:flex;align-items:center;justify-content:center}
.role{position:absolute;font-size:5px;color:var(--magenta);text-align:center}
</style>
</head>
<body>

<div class="brand-hero">Vantreo</div>
<div class="tagline">SINGLE TEMPLATE FOR ALL YOUR PRESENTATIONS</div>
<div class="feature blue" style="left:320px">ppt and<br>pptx files</div>
<div class="feature green" style="left:434px">all vector<br>icons</div>
<div class="feature violet" style="left:549px">Multiple<br>colors</div>
<div class="feature magenta" style="left:665px">Master<br>slide easy<br>editable</div>
<div class="feature slate" style="left:787px">Fonts<br>included</div>

<!-- title slide large -->
<section class="slide" style="left:71px;top:476px;width:696px;height:391px">
  <div class="photo round" role="img" aria-label="Two engineers with a laptop in a server room" style="left:347px;top:-70px;width:520px;height:520px"></div>
  <div class="abs wordmark" style="left:36px;top:112px;font-size:46px">Vantreo</div>
  <div class="abs headline" style="left:36px;top:216px;font-size:17px;line-height:23px">Your slide title goes on<br>these two lines</div>
  <div class="abs" style="left:36px;top:270px;font-size:10.5px;line-height:15px;width:240px">Lorem ipsum dolor sit amet, consectetur adipiscing elit, sed do eiusmod tempor incididunt ut labore et dolore magna aliqua.</div>
  <div class="abs url" style="left:38px;top:354px">www.vantreo.info</div>
  <div class="strip"></div>
</section>

<!-- title slide small -->
<section class="slide" style="left:780px;top:476px;width:341px;height:189px">
  <div class="photo round" role="img" aria-label="Engineers in a server room" style="left:145px;top:2px;width:185px;height:185px"></div>
  <div class="abs wordmark" style="left:22px;top:52px;font-size:22px">Vantreo</div>
  <div class="abs headline" style="left:22px;top:105px;font-size:8px;line-height:11px">Your slide title goes on<br>these two lines</div>
  <div class="abs tiny" style="left:22px;top:131px;width:120px;line-height:6px">Lorem ipsum dolor sit amet, consectetur adipiscing elit, sed do eiusmod tempor incididunt ut labore et dolore magna aliqua.</div>
  <div class="abs url" style="left:22px;top:166px;font-size:5px;letter-spacing:1.5px">www.vantreo.info</div>
  <div class="strip"></div>
</section>

<!-- title slide blue -->
<section class="slide" style="left:780px;top:675px;width:341px;height:192px;background:var(--blue)">
  <div class="abs wordmark" style="left:46px;top:96px;font-size:24px;color:var(--white)">Vantreo</div>
  <div class="abs" style="left:160px;top:60px;font-family:Montserrat,Arial,sans-serif;font-weight:600;font-size:8.5px;line-height:12px;color:var(--white)">YOUR SLIDE TITLE GOES ON<br>THESE TWO LINES</div>
  <div class="abs" style="left:160px;top:88px;width:120px;font-size:5px;line-height:6.5px;color:#dcecf8">Lorem ipsum dolor sit amet, consectetur adipiscing elit, sed do eiusmod tempor incididunt ut labore et dolore magna aliqua.</div>
  <div class="abs url" style="left:160px;top:134px;font-size:5px;letter-spacing:1.5px;color:var(--white)">www.vantreo.info</div>
  <div class="strip"></div>
</section>

<!-- icon style preview -->
<section class="slide" style="left:71px;top:880px;width:517px;height:289px">
  <div class="title" style="left:24px;top:18px;font-size:13px">Icon Style Preview</div>
  <div class="subtitle" style="left:24px;top:37px;font-size:7px">Lorem ipsum dolor sit amet, consectetur adipiscing elit</div>
  <div class="mini-brand" style="top:24px;font-size:8px">Vantreo</div>
  <svg width="517" height="289" viewBox="0 0 517 289" style="left:0;top:0" fill="none" stroke="currentColor" stroke-width="1.2" stroke-linecap="round" stroke-linejoin="round">
    <defs>
      <symbol id="i-clock" viewBox="0 0 20 20"><circle cx="10" cy="11" r="7"/><path d="M10 7v4l3 2"/></symbol>
      <symbol id="i-doc" viewBox="0 0 20 20"><path d="M5 2h7l4 4v12H5z"/><path d="M12 2v4h4"/></symbol>
      <symbol id="i-plus" viewBox="0 0 20 20"><circle cx="10" cy="10" r="8"/><path d="M10 6v8M6 10h8"/></symbol>
      <symbol id="i-pin" viewBox="0 0 20 20"><path d="M10 18s6-6 6-10a6 6 0 0 0-12 0c0 4 6 10 6 10z"/><circle cx="10" cy="8" r="2"/></symbol>
      <symbol id="i-lock" viewBox="0 0 20 20"><rect x="4" y="9" width="12" height="9" rx="1"/><path d="M7 9V6a3 3 0 0 1 6 0v3"/></symbol>
      <symbol id="i-image" viewBox="0 0 20 20"><rect x="2" y="4" width="16" height="12"/><path d="M2 14l5-5 4 4 3-3 4 4"/></symbol>
      <symbol id="i-cloud" viewBox="0 0 20 20"><path d="M5 15h10a3 3 0 0 0 0-6 5 5 0 0 0-9.5-1A3.5 3.5 0 0 0 5 15z"/></symbol>
      <symbol id="i-heart" viewBox="0 0 20 20"><path d="M10 17S3 12 3 7.5A3.5 3.5 0 0 1 10 6a3.5 3.5 0 0 1 7 1.5C17 12 10 17 10 17z"/></symbol>
      <symbol id="i-grid" viewBox="0 0 20 20"><circle cx="5" cy="5" r="1.5"/><circle cx="10" cy="5" r="1.5"/><circle cx="15" cy="5" r="1.5"/><circle cx="5" cy="10" r="1.5"/><circle cx="10" cy="10" r="1.5"/><circle cx="15" cy="10" r="1.5"/><circle cx="5" cy="15" r="1.5"/><circle cx="10" cy="15" r="1.5"/><circle cx="15" cy="15" r="1.5"/></symbol>
      <symbol id="i-slider" viewBox="0 0 20 20"><path d="M5 3v14M10 3v14M15 3v14"/><rect x="3" y="6" width="4" height="3"/><rect x="8" y="11" width="4" height="3"/><rect x="13" y="7" width="4" height="3"/></symbol>
      <symbol id="i-search" viewBox="0 0 20 20"><circle cx="8" cy="8" r="5.5"/><path d="M12 12l6 6"/></symbol>
      <symbol id="i-box" viewBox="0 0 20 20"><rect x="3" y="3" width="14" height="14" rx="1"/><path d="M3 8h14M8 8v9"/></symbol>
    </defs>
    <g>
      <use href="#i-clock" class="g" x="25" y="76" width="18" height="18"/><use href="#i-search" class="b" x="66" y="76" width="18" height="18"/><use href="#i-clock" class="v" x="106" y="76" width="18" height="18"/><use href="#i-clock" class="g" x="147" y="76" width="18" height="18"/><use href="#i-clock" class="m" x="187" y="76" width="18" height="18"/><use href="#i-clock" class="m" x="228" y="76" width="18" height="18"/><use href="#i-search" class="b" x="268" y="76" width="18" height="18"/><use href="#i-search" class="v" x="309" y="76" width="18" height="18"/><use href="#i-plus" class="g" x="349" y="76" width="18" height="18"/><use href="#i-plus" class="g" x="390" y="76" width="18" height="18"/><use href="#i-plus" class="b" x="430" y="76" width="18" height="18"/><use href="#i-plus" class="m" x="471" y="76" width="18" height="18"/>
      <use href="#i-doc" class="g" x="25" y="107" width="18" height="18"/><use href="#i-doc" class="b" x="66" y="107" width="18" height="18"/><use href="#i-doc" class="v" x="106" y="107" width="18" height="18"/><use href="#i-image" class="g" x="147" y="107" width="18" height="18"/><use href="#i-heart" class="m" x="187" y="107" width="18" height="18"/><use href="#i-box" class="m" x="228" y="107" width="18" height="18"/><use href="#i-doc" class="b" x="268" y="107" width="18" height="18"/><use href="#i-box" class="v" x="309" y="107" width="18" height="18"/><use href="#i-box" class="g" x="349" y="107" width="18" height="18"/><use href="#i-plus" class="g" x="390" y="107" width="18" height="18"/><use href="#i-plus" class="b" x="430" y="107" width="18" height="18"/><use href="#i-plus" class="m" x="471" y="107" width="18" height="18"/>
      <use href="#i-pin" class="g" x="25" y="139" width="18" height="18"/><use href="#i-image" class="b" x="66" y="139" width="18" height="18"/><use href="#i-slider" class="v" x="106" y="139" width="18" height="18"/><use href="#i-pin" class="g" x="147" y="139" width="18" height="18"/><use href="#i-pin" class="m" x="187" y="139" width="18" height="18"/><use href="#i-box" class="m" x="228" y="139" width="18" height="18"/><use href="#i-grid" class="b" x="268" y="139" width="18" height="18"/><use href="#i-search" class="v" x="309" y="139" width="18" height="18"/><use href="#i-grid" class="g" x="349" y="139" width="18" height="18"/><use href="#i-lock" class="g" x="390" y="139" width="18" height="18"/><use href="#i-lock" class="b" x="430" y="139" width="18" height="18"/><use href="#i-lock" class="m" x="471" y="139" width="18" height="18"/>
      <use href="#i-cloud" class="g" x="25" y="171" width="18" height="18"/><use href="#i-search" class="b" x="66" y="171" width="18" height="18"/><use href="#i-search" class="v" x="106" y="171" width="18" height="18"/><use href="#i-doc" class="g" x="147" y="171" width="18" height="18"/><use href="#i-image" class="m" x="187" y="171" width="18" height="18"/><use href="#i-image" class="m" x="228" y="171" width="18" height="18"/><use href="#i-grid" class="b" x="268" y="171" width="18" height="18"/><use href="#i-grid" class="v" x="309" y="171" width="18" height="18"/><use href="#i-clock" class="g" x="349" y="171" width="18" height="18"/><use href="#i-pin" class="g" x="390" y="171" width="18" height="18"/><use href="#i-plus" class="b" x="430" y="171" width="18" height="18"/><use href="#i-doc" class="m" x="471" y="171" width="18" height="18"/>
      <use href="#i-doc" class="g" x="25" y="202" width="18" height="18"/><use href="#i-lock" class="b" x="66" y="202" width="18" height="18"/><use href="#i-lock" class="v" x="106" y="202" width="18" height="18"/><use href="#i-heart" class="g" x="147" y="202" width="18" height="18"/><use href="#i-cloud" class="m" x="187" y="202" width="18" height="18"/><use href="#i-cloud" class="m" x="228" y="202" width="18" height="18"/><use href="#i-cloud" class="b" x="268" y="202" width="18" height="18"/><use href="#i-image" class="v" x="309" y="202" width="18" height="18"/><use href="#i-image" class="g" x="349" y="202" width="18" height="18"/><use href="#i-image" class="g" x="390" y="202" width="18" height="18"/><use href="#i-image" class="b" x="430" y="202" width="18" height="18"/><use href="#i-pin" class="m" x="471" y="202" width="18" height="18"/>
      <use href="#i-slider" class="g" x="25" y="234" width="18" height="18"/><use href="#i-slider" class="b" x="66" y="234" width="18" height="18"/><use href="#i-box" class="v" x="106" y="234" width="18" height="18"/><use href="#i-box" class="g" x="147" y="234" width="18" height="18"/><use href="#i-box" class="m" x="187" y="234" width="18" height="18"/><use href="#i-box" class="m" x="228" y="234" width="18" height="18"/><use href="#i-doc" class="b" x="268" y="234" width="18" height="18"/><use href="#i-clock" class="v" x="309" y="234" width="18" height="18"/><use href="#i-pin" class="g" x="349" y="234" width="18" height="18"/><use href="#i-doc" class="g" x="390" y="234" width="18" height="18"/><use href="#i-plus" class="b" x="430" y="234" width="18" height="18"/><use href="#i-clock" class="m" x="471" y="234" width="18" height="18"/>
    </g>
  </svg>
  <div class="strip"></div>
</section>

<!-- agenda -->
<section class="slide" style="left:610px;top:880px;width:511px;height:289px">
  <div class="title" style="left:24px;top:18px;font-size:13px">PRESENTATION AGENDA</div>
  <div class="subtitle" style="left:24px;top:37px;font-size:7px">Lorem ipsum dolor sit amet, consectetur adipiscing elit</div>
  <div class="mini-brand" style="top:24px;font-size:8px">Vantreo</div>

  <div class="agenda-num" style="left:54px;top:79px;background:var(--blue)">1</div>
  <div class="agenda-label" style="left:54px;top:103px">Lorem Ipsum</div>
  <div class="agenda-desc" style="left:54px;top:120px">Lorem Ipsum is simply dummy text of the printing and typesetting industry.</div>
  <div class="agenda-num" style="left:193px;top:79px;background:var(--green)">3</div>
  <div class="agenda-label" style="left:193px;top:103px">Lorem Ipsum</div>
  <div class="agenda-desc" style="left:193px;top:120px">Lorem Ipsum is simply dummy text of the printing and typesetting industry.</div>
  <div class="agenda-num" style="left:340px;top:79px;background:var(--magenta)">5</div>
  <div class="agenda-label" style="left:340px;top:103px">Lorem Ipsum</div>
  <div class="agenda-desc" style="left:340px;top:120px">Lorem Ipsum is simply dummy text of the printing and typesetting industry.</div>

  <div class="agenda-num" style="left:54px;top:177px;background:var(--blue)">2</div>
  <div class="agenda-label" style="left:54px;top:201px">Lorem Ipsum</div>
  <div class="agenda-desc" style="left:54px;top:218px">Lorem Ipsum is simply dummy text of the printing and typesetting industry.</div>
  <div class="agenda-num" style="left:193px;top:177px;background:var(--green)">4</div>
  <div class="agenda-label" style="left:193px;top:201px">Lorem Ipsum</div>
  <div class="agenda-desc" style="left:193px;top:218px">Lorem Ipsum is simply dummy text of the printing and typesetting industry.</div>
  <div class="agenda-num" style="left:340px;top:177px;background:var(--magenta)">6</div>
  <div class="agenda-label" style="left:340px;top:201px">Lorem Ipsum</div>
  <div class="agenda-desc" style="left:340px;top:218px">Lorem Ipsum is simply dummy text of the printing and typesetting industry.</div>

  <div class="foot" style="left:16px;bottom:12px;font-size:5px">© 2018 Vantreo. All Rights Reserved.</div>
  <div class="page" style="bottom:12px;font-size:5px">01</div>
  <div class="strip"></div>
</section>

<!-- quote slide -->
<section class="slide" style="left:71px;top:1188px;width:340px;height:192px">
  <div class="photo" role="img" aria-label="Hands typing on a laptop keyboard" style="left:0;top:0;width:340px;height:107px"></div>
  <div class="abs wordmark" style="left:42px;top:48px;font-size:15px;color:var(--white)">Vantreo</div>
  <div class="abs" style="left:0;top:107px;width:340px;height:85px;background:var(--blue)"></div>
  <div class="abs" style="left:40px;top:125px;width:230px;font-size:5.5px;line-height:8px;color:var(--white)">Lorem Ipsum is simply dummy text of the printing and typesetting industry. Lorem Ipsum is simply dummy text of the printing and typesetting industry. Lorem Ipsum is simply dummy text of the printing and typesetting industry.</div>
  <div class="abs" style="left:40px;top:164px;font-size:5px;color:var(--white)">- Lorem Ipsum</div>
  <div class="abs" style="left:258px;top:146px;font-family:Montserrat,Arial,sans-serif;font-weight:700;font-size:26px;color:var(--white)">“”</div>
  <div class="strip"></div>
</section>

<!-- two column -->
<section class="slide" style="left:426px;top:1188px;width:340px;height:192px">
  <div class="title">Two Column</div>
  <div class="subtitle">Lorem ipsum dolor sit amet, consectetur adipiscing elit</div>
  <div class="mini-brand">Vantreo</div>
  <svg width="20" height="150" style="left:20px;top:44px" fill="none" stroke-width="1">
    <circle cx="4" cy="4" r="2.5" stroke="var(--blue)"/><circle cx="4" cy="19" r="2.5" stroke="var(--green)"/><circle cx="4" cy="34" r="2.5" stroke="var(--magenta)"/><circle cx="4" cy="50" r="2.5" stroke="var(--blue)"/><circle cx="4" cy="65" r="2.5" stroke="var(--green)"/><circle cx="4" cy="80" r="2.5" stroke="var(--magenta)"/><circle cx="4" cy="96" r="2.5" stroke="var(--blue)"/><circle cx="4" cy="111" r="2.5" stroke="var(--green)"/>
  </svg>
  <div class="abs tiny" style="left:34px;top:44px;width:140px;font-size:4px;line-height:7.7px">
    Lorem Ipsum is simply dummy text of the printing and typesetting industry.<br>Lorem Ipsum is simply dummy text of the printing and typesetting industry.<br>Lorem Ipsum is simply dummy text of the printing and typesetting industry.<br>Lorem Ipsum is simply dummy text of the printing and typesetting industry.<br>Lorem Ipsum is simply dummy text of the printing and typesetting industry.<br>Lorem Ipsum is simply dummy text of the printing and typesetting industry.<br>Lorem Ipsum is simply dummy text of the printing and typesetting industry.<br>Lorem Ipsum is simply dummy text of the printing and typesetting industry.
  </div>
  <div class="photo round" role="img" aria-label="Two engineers in a server room" style="left:181px;top:28px;width:143px;height:143px"></div>
  <div class="foot">© 2018 Vantreo. All Rights Reserved.</div><div class="page">02</div>
  <div class="strip"></div>
</section>

<!-- three column -->
<section class="slide" style="left:780px;top:1188px;width:341px;height:192px">
  <div class="title">Three Column</div>
  <div class="subtitle">Lorem ipsum dolor sit amet, consectetur adipiscing elit</div>
  <div class="mini-brand">Vantreo</div>
  <div class="photo round" role="img" aria-label="Engineers in a server room" style="left:-70px;top:38px;width:190px;height:190px"></div>
  <div class="abs tiny" style="left:140px;top:47px;width:82px;font-size:4px;line-height:6px">Lorem Ipsum is simply dummy text of the printing and typesetting industry. Lorem Ipsum is simply dummy text of the printing and typesetting industry.<br><br>Lorem Ipsum is simply dummy text of the printing and typesetting industry. Lorem Ipsum is simply dummy text of the printing and typesetting industry.<br><br>Lorem Ipsum is simply dummy text of the printing and typesetting industry. Lorem Ipsum is simply dummy text of the printing and typesetting industry.</div>
  <div class="abs tiny" style="left:239px;top:47px;width:82px;font-size:4px;line-height:6px">Lorem Ipsum is simply dummy text of the printing and typesetting industry. Lorem Ipsum is simply dummy text of the printing and typesetting industry.<br><br>Lorem Ipsum is simply dummy text of the printing and typesetting industry. Lorem Ipsum is simply dummy text of the printing and typesetting industry.<br><br>Lorem Ipsum is simply dummy text of the printing and typesetting industry. Lorem Ipsum is simply dummy text of the printing and typesetting industry.</div>
  <div class="page">03</div>
  <div class="strip"></div>
</section>

<!-- presenter -->
<section class="slide" style="left:71px;top:1399px;width:340px;height:191px">
  <div class="photo" role="img" aria-label="Smiling presenter with colleagues" style="left:0;top:0;width:125px;height:191px;background:linear-gradient(135deg,#5f7c9c,#9fb6cc 60%,#d7dfe7)"></div>
  <div class="abs" style="left:121px;top:14px;width:71px;height:152px;background:var(--magenta)"></div>
  <div class="abs" style="left:128px;top:20px;font-size:10px;color:#e4b6dc;letter-spacing:-1px">»»</div>
  <div class="abs" style="left:128px;top:40px;width:58px;font-size:4px;line-height:5.5px;color:var(--white)">Lorem Ipsum is simply dummy text of the printing and typesetting industry. Lorem Ipsum has been the industry's standard dummy text ever since the 1500s. Lorem Ipsum is simply dummy text of the printing and typesetting industry.<br><br>Lorem Ipsum is simply dummy text of the printing and typesetting industry.</div>
  <div class="abs" style="left:211px;top:36px;font-weight:600;font-size:9px">Presenter Name</div>
  <div class="abs tiny" style="left:211px;top:48px;width:90px;font-size:4px;line-height:5.5px;color:var(--muted)">Lorem ipsum dolor sit amet, consectetur adipiscing elit</div>
  <div class="abs tiny" style="left:211px;top:64px;width:112px;font-size:4px;line-height:5.5px">Lorem Ipsum is simply dummy text of the printing and typesetting industry. Lorem Ipsum is simply dummy text of the printing and typesetting industry. Lorem Ipsum is simply dummy text of the printing and typesetting industry.</div>
  <div class="abs tiny" style="left:226px;top:115px;width:97px;font-size:4px;line-height:5px">Lorem Ipsum is simply dummy text of the printing and typesetting industry.<br><br>Lorem Ipsum is simply dummy text of the printing and typesetting industry.<br><br>Lorem Ipsum is simply dummy text of the printing and typesetting industry.</div>
  <svg width="10" height="60" style="left:213px;top:115px" fill="none" stroke-width="0.8"><circle cx="4" cy="3" r="2.5" stroke="var(--magenta)"/><circle cx="4" cy="18" r="2.5" stroke="var(--magenta)"/><circle cx="4" cy="33" r="2.5" stroke="var(--magenta)"/><circle cx="4" cy="48" r="2.5" stroke="var(--magenta)"/></svg>
  <div class="mini-brand">Vantreo</div>
  <div class="strip"></div>
</section>

<!-- price packages (icons) -->
<section class="slide" style="left:426px;top:1399px;width:340px;height:191px">
  <div class="title">Price Packages Slide</div>
  <div class="subtitle">Lorem ipsum dolor sit amet, consectetur adipiscing elit</div>
  <div class="mini-brand">Vantreo</div>
  <div class="photo round" role="img" aria-label="Developer working on a laptop" style="left:23px;top:52px;width:105px;height:105px;background:linear-gradient(135deg,#385a78,#7fa2bf 60%,#c3d3e0)"></div>
  <svg width="200" height="120" style="left:134px;top:55px">
    <circle cx="13" cy="13" r="13" fill="var(--blue)"/><circle cx="28" cy="49" r="13" fill="var(--green)"/><circle cx="17" cy="86" r="13" fill="var(--magenta)"/>
    <g fill="none" stroke="#fff" stroke-width="1.2"><path d="M7 12a8 8 0 0 1 12 0M9.5 14.5a4.5 4.5 0 0 1 7 0"/><circle cx="13" cy="17.5" r="0.8" fill="#fff"/><rect x="22" y="44" width="12" height="10"/><rect x="11" y="81" width="12" height="10"/></g>
  </svg>
  <div class="abs tiny" style="left:180px;top:60px;width:140px;font-size:4px;line-height:5.5px">Lorem Ipsum is simply dummy text of the printing and typesetting industry. Lorem Ipsum is simply dummy text of the printing and typesetting industry.</div>
  <div class="abs tiny" style="left:190px;top:97px;width:132px;font-size:4px;line-height:5.5px">Lorem Ipsum is simply dummy text of the printing and typesetting industry. Lorem Ipsum is simply dummy text of the printing and typesetting industry.</div>
  <div class="abs tiny" style="left:180px;top:134px;width:140px;font-size:4px;line-height:5.5px">Lorem Ipsum is simply dummy text of the printing and typesetting industry. Lorem Ipsum is simply dummy text of the printing and typesetting industry.</div>
  <div class="foot">© 2018 Vantreo. All Rights Reserved.</div><div class="page">05</div>
  <div class="strip"></div>
</section>

<!-- infographics -->
<section class="slide" style="left:780px;top:1399px;width:341px;height:191px">
  <div class="title">Infographics</div>
  <div class="subtitle">Lorem ipsum dolor sit amet, consectetur adipiscing elit</div>
  <div class="mini-brand">Vantreo</div>
  <svg width="341" height="130" style="left:0;top:40px" fill="none" stroke="#b9bbbe" stroke-width="0.8">
    <line x1="36" y1="18" x2="36" y2="100"/><line x1="80" y1="60" x2="80" y2="100"/><line x1="124" y1="18" x2="124" y2="100"/><line x1="169" y1="60" x2="169" y2="100"/><line x1="213" y1="18" x2="213" y2="100"/><line x1="257" y1="60" x2="257" y2="100"/><line x1="301" y1="18" x2="301" y2="100"/>
    <line x1="20" y1="100" x2="320" y2="100"/>
  </svg>
  <div class="photo round" role="img" aria-label="Team member portrait" style="left:68px;top:49px;width:30px;height:30px"></div>
  <div class="photo round" role="img" aria-label="Team member portrait" style="left:156px;top:49px;width:30px;height:30px"></div>
  <div class="photo round" role="img" aria-label="Team member portrait" style="left:244px;top:49px;width:30px;height:30px"></div>
  <div class="abs tiny" style="left:20px;top:46px;width:34px;font-size:3.5px;line-height:4.5px;text-align:center">Lorem Ipsum is simply dummy text of the printing and typesetting industry</div>
  <div class="abs tiny" style="left:107px;top:46px;width:34px;font-size:3.5px;line-height:4.5px;text-align:center">Lorem Ipsum is simply dummy text of the printing and typesetting industry</div>
  <div class="abs tiny" style="left:196px;top:46px;width:34px;font-size:3.5px;line-height:4.5px;text-align:center">Lorem Ipsum is simply dummy text of the printing and typesetting industry</div>
  <div class="abs tiny" style="left:284px;top:46px;width:34px;font-size:3.5px;line-height:4.5px;text-align:center">Lorem Ipsum is simply dummy text of the printing and typesetting industry</div>
  <div class="abs tiny" style="left:63px;top:92px;width:34px;font-size:3.5px;line-height:4.5px;text-align:center">Lorem Ipsum is simply dummy text of the printing and typesetting</div>
  <div class="abs tiny" style="left:152px;top:92px;width:34px;font-size:3.5px;line-height:4.5px;text-align:center">Lorem Ipsum is simply dummy text of the printing and typesetting</div>
  <div class="abs tiny" style="left:240px;top:92px;width:34px;font-size:3.5px;line-height:4.5px;text-align:center">Lorem Ipsum is simply dummy text of the printing and typesetting</div>
  <div class="abs" style="left:24px;top:146px;width:300px;display:flex;justify-content:space-between;font-size:7.5px;color:var(--slate)"><span>2000</span><span>2002</span><span>2004</span><span>2006</span><span>2008</span><span>2012</span><span>2015</span></div>
  <div class="foot">© 2018 Vantreo. All Rights Reserved.</div><div class="page">06</div>
  <div class="strip"></div>
</section>

<!-- mobile app -->
<section class="slide" style="left:71px;top:1609px;width:340px;height:192px">
  <div class="title">Mobile App Screen Slide</div>
  <div class="subtitle">Lorem ipsum dolor sit amet, consectetur adipiscing elit</div>
  <div class="mini-brand">Vantreo</div>
  <div class="abs tiny" style="left:15px;top:46px;width:160px;font-size:4px;line-height:5.5px">Lorem Ipsum is simply dummy text of the printing and typesetting industry. Lorem Ipsum is simply dummy text of the printing and typesetting industry. Lorem Ipsum is simply dummy text of the printing and typesetting industry. Lorem Ipsum is simply dummy text of the printing.</div>
  <svg width="24" height="70" style="left:33px;top:92px" fill="none" stroke-width="1">
    <rect x="2" y="2" width="14" height="12" stroke="var(--blue)"/><path d="M6 2v12M12 2v12" stroke="var(--blue)"/>
    <path d="M3 34a6 5 0 0 1 11-2 4 4 0 0 1 1 8H5a3 3 0 0 1-2-6z" stroke="var(--green)"/>
    <path d="M3 57a6 5 0 0 1 11-2 4 4 0 0 1 1 8H5a3 3 0 0 1-2-6z" stroke="var(--magenta)"/>
  </svg>
  <div class="abs tiny" style="left:64px;top:95px;width:110px;font-size:4px;line-height:5.5px">Lorem Ipsum is simply dummy text of the printing and typesetting industry.</div>
  <div class="abs tiny" style="left:64px;top:120px;width:110px;font-size:4px;line-height:5.5px">Lorem Ipsum is simply dummy text of the printing and typesetting industry.</div>
  <div class="abs tiny" style="left:64px;top:145px;width:110px;font-size:4px;line-height:5.5px">Lorem Ipsum is simply dummy text of the printing and typesetting industry.</div>
  <svg width="120" height="130" style="left:210px;top:42px" fill="none" stroke="var(--ink)" stroke-width="3">
    <rect x="4" y="3" width="50" height="110" rx="8"/>
    <rect x="61" y="20" width="50" height="108" rx="8"/>
  </svg>
  <div class="foot">© 2018 Vantreo. All Rights Reserved.</div><div class="page">07</div>
  <div class="strip"></div>
</section>

<!-- dashboard / video -->
<section class="slide" style="left:426px;top:1609px;width:340px;height:192px">
  <div class="title">Dashboard or Video Slide</div>
  <div class="subtitle">Lorem ipsum dolor sit amet, consectetur adipiscing elit</div>
  <div class="mini-brand">Vantreo</div>
  <svg width="215" height="130" style="left:2px;top:45px" fill="none">
    <rect x="11" y="1" width="188" height="110" rx="3" stroke="#9a9c9f" stroke-width="1.2" fill="#fbfbfb"/>
    <rect x="17" y="7" width="176" height="98" fill="#fff" stroke="#d5d7d9" stroke-width="0.6"/>
    <path d="M0 113h210l-6 7H6z" fill="#c4c6c9"/>
    <circle cx="105" cy="56" r="10" stroke="var(--magenta)" stroke-width="1"/>
    <path d="M101.5 51v10l8.5-5z" stroke="var(--magenta)" stroke-width="1" stroke-linejoin="round"/>
  </svg>
  <div class="abs tiny" style="left:224px;top:74px;width:102px;font-size:4.5px;line-height:6.5px">Lorem Ipsum is simply dummy text of the printing and typesetting industry. Lorem Ipsum is simply dummy text of the printing and typesetting industry. Lorem Ipsum is simply dummy text of the printing and typesetting industry.</div>
  <div class="foot">© 2018 Vantreo. All Rights Reserved.</div><div class="page">08</div>
  <div class="strip"></div>
</section>

<!-- price packages (table) -->
<section class="slide" style="left:780px;top:1609px;width:341px;height:192px">
  <div class="title">Price Packages Slide</div>
  <div class="subtitle">Lorem ipsum dolor sit amet, consectetur adipiscing elit</div>
  <div class="mini-brand">Vantreo</div>
  <div class="plan" style="left:16px;background:#4a4b4d"><div class="name">FREE</div><div class="price"><sup>$</sup>0</div></div>
  <div class="plan" style="left:92px;background:var(--blue)"><div class="name">STANDARD</div><div class="price"><sup>$</sup>6</div></div>
  <div class="plan" style="left:170px;background:var(--green)"><div class="name">PLUS</div><div class="price"><sup>$</sup>12</div></div>
  <div class="plan" style="left:247px;background:var(--magenta)"><div class="name">ENTERPRISE</div><div class="price"><sup>$</sup>20</div></div>
  <div class="plan-body" style="left:16px"><p>Lorem ipsum is simply</p><p>Dummy text of the printing</p><p>Lorem ipsum is simply dummy text of the</p><p>Printing and typesetting</p></div>
  <div class="plan-body" style="left:92px"><p>Lorem ipsum is simply</p><p>Dummy text of the printing</p><p>Lorem ipsum is simply dummy text of the</p><p>Printing and typesetting</p></div>
  <div class="plan-body" style="left:170px"><p>Lorem ipsum is simply</p><p>Dummy text of the printing</p><p>Lorem ipsum is simply dummy text of the</p><p>Printing and typesetting</p></div>
  <div class="plan-body" style="left:247px"><p>Lorem ipsum is simply</p><p>Dummy text of the printing</p><p>Lorem ipsum is simply dummy text of the</p><p>Printing and typesetting</p></div>
  <div class="foot">© 2018 Vantreo. All Rights Reserved.</div><div class="page">09</div>
  <div class="strip"></div>
</section>

<!-- feature slide large -->
<section class="slide" style="left:71px;top:1820px;width:696px;height:397px">
  <div class="photo" role="img" aria-label="Developers working at computer screens" style="left:0;top:0;width:696px;height:397px;background:linear-gradient(120deg,#264a6e 0%,#3c6f99 35%,#b9c8d6 70%,#6a7f94 100%)"></div>
  <div class="abs" style="left:57px;top:0;width:252px;height:397px;background:var(--blue)"></div>
  <div class="abs" style="left:77px;top:44px;width:200px;font-size:16.5px;line-height:22px;color:var(--white)">Lorem Ipsum Dolor Sit Amet, Consectetur Adipiscing Elit</div>
  <svg width="40" height="200" style="left:80px;top:142px" fill="none" stroke="#fff" stroke-width="1.3">
    <rect x="2" y="2" width="30" height="24" rx="1"/><path d="M12 2v24M22 2v24M4 8h6M14 8h6M24 8h6"/>
    <path d="M5 104a9 8 0 0 1 17-3 7 7 0 0 1 3 13H7a5 5 0 0 1-2-10z"/><path d="M10 108l-4 4 4 4M20 108l4 4-4 4"/>
    <path d="M5 176a9 8 0 0 1 17-3 7 7 0 0 1 3 13H7a5 5 0 0 1-2-10z"/><rect x="11" y="182" width="10" height="9"/><path d="M13 182v-3a3 3 0 0 1 6 0v3"/>
  </svg>
  <div class="abs" style="left:135px;top:141px;width:110px;font-size:10px;line-height:13.5px;color:var(--white)">Lorem Ipsum is simply dummy text of the printing and typesetting industry.</div>
  <div class="abs" style="left:135px;top:222px;width:110px;font-size:10px;line-height:13.5px;color:var(--white)">Lorem Ipsum is simply dummy text of the printing and typesetting industry.</div>
  <div class="abs" style="left:135px;top:300px;width:110px;font-size:10px;line-height:13.5px;color:var(--white)">Lorem Ipsum is simply dummy text of the printing and typesetting industry.</div>
  <div class="photo" role="img" aria-label="Hands on a laptop and notepad" style="left:257px;top:131px;width:156px;height:226px;background:linear-gradient(150deg,#2f4f6e,#5f86a8 55%,#1c3046)"></div>
  <div class="abs" style="left:413px;top:131px;width:215px;height:266px;background:var(--white)"></div>
  <div class="abs" style="left:445px;top:160px;width:170px;font-size:7px;line-height:10px;color:var(--slate)">Lorem Ipsum is simply dummy text of the printing and typesetting industry. Lorem Ipsum is simply dummy text of the printing and typesetting industry. Lorem Ipsum is simply dummy text of the printing and typesetting industry. Lorem Ipsum is simply dummy text of the printing and typesetting industry.</div>
  <svg width="16" height="100" style="left:447px;top:244px" fill="none" stroke-width="1">
    <path d="M3 5a4 4 0 0 1 8 0M3 5l-1 3M11 5l1 3" stroke="var(--blue)"/><path d="M3 30a4 4 0 0 1 8 0M3 30l-1 3M11 30l1 3" stroke="var(--green)"/><path d="M3 55a4 4 0 0 1 8 0M3 55l-1 3M11 55l1 3" stroke="var(--blue)"/><path d="M3 80a4 4 0 0 1 8 0M3 80l-1 3M11 80l1 3" stroke="var(--violet)"/>
  </svg>
  <div class="abs" style="left:470px;top:243px;width:150px;font-size:6px;line-height:8.5px;color:var(--slate)">Lorem Ipsum is simply dummy text of the printing and typesetting industry.</div>
  <div class="abs" style="left:470px;top:268px;width:150px;font-size:6px;line-height:8.5px;color:var(--slate)">Lorem Ipsum is simply dummy text of the printing and typesetting industry.</div>
  <div class="abs" style="left:470px;top:293px;width:150px;font-size:6px;line-height:8.5px;color:var(--slate)">Lorem Ipsum is simply dummy text of the printing and typesetting industry.</div>
  <div class="abs" style="left:470px;top:318px;width:150px;font-size:6px;line-height:8.5px;color:var(--slate)">Lorem Ipsum is simply dummy text of the printing and typesetting industry.</div>
</section>

<!-- timeline -->
<section class="slide" style="left:780px;top:1820px;width:341px;height:190px">
  <div class="title">Timeline/steps Slide</div>
  <div class="subtitle">Lorem ipsum dolor sit amet, consectetur adipiscing elit</div>
  <div class="mini-brand">Vantreo</div>
  <div class="abs tiny" style="left:18px;top:54px;width:54px;font-size:4px;line-height:5px;text-align:center">Lorem Ipsum is simply dummy text of the printing and typesetting industry.</div>
  <div class="abs tiny" style="left:118px;top:54px;width:54px;font-size:4px;line-height:5px;text-align:center">Lorem Ipsum is simply dummy text of the printing and typesetting industry.</div>
  <div class="abs tiny" style="left:220px;top:54px;width:54px;font-size:4px;line-height:5px;text-align:center">Lorem Ipsum is simply dummy text of the printing and typesetting industry.</div>
  <div class="abs" style="left:88px;top:64px;font-size:13px;color:var(--blue)">2</div>
  <div class="abs" style="left:191px;top:64px;font-size:13px;color:var(--blue)">4</div>
  <div class="abs" style="left:292px;top:64px;font-size:13px;color:var(--blue)">6</div>
  <svg width="341" height="40" style="left:0;top:90px" fill="none">
    <circle cx="42" cy="13" r="12" fill="var(--magenta)"/><circle cx="93" cy="13" r="12" fill="var(--green)"/><circle cx="145" cy="13" r="12" fill="var(--magenta)"/><circle cx="196" cy="13" r="12" fill="var(--green)"/><circle cx="247" cy="13" r="12" fill="var(--magenta)"/><circle cx="299" cy="13" r="12" fill="var(--green)"/>
    <g fill="var(--blue)"><path d="M62 10l5 3-5 3z"/><path d="M113 10l5 3-5 3z"/><path d="M165 10l5 3-5 3z"/><path d="M216 10l5 3-5 3z"/><path d="M267 10l5 3-5 3z"/></g>
    <g stroke="#fff" stroke-width="1"><circle cx="42" cy="11" r="3"/><path d="M37 19a5 4 0 0 1 10 0"/><path d="M88 16l10-7-3 10-2-3z"/><circle cx="145" cy="12" r="4"/><path d="M143 17h4"/><ellipse cx="196" cy="9" rx="5" ry="2"/><path d="M191 9v8c0 1 2 2 5 2s5-1 5-2V9"/><rect x="242" y="8" width="10" height="10"/><path d="M299 7l2 4 4 .5-3 3 1 4-4-2-4 2 1-4-3-3 4-.5z"/></g>
  </svg>
  <div class="abs" style="left:37px;top:126px;font-size:13px;color:var(--blue)">1</div>
  <div class="abs" style="left:140px;top:126px;font-size:13px;color:var(--blue)">3</div>
  <div class="abs" style="left:242px;top:126px;font-size:13px;color:var(--blue)">5</div>
  <div class="abs tiny" style="left:66px;top:130px;width:54px;font-size:4px;line-height:5px;text-align:center">Lorem Ipsum is simply dummy text of the printing and typesetting industry.</div>
  <div class="abs tiny" style="left:168px;top:130px;width:54px;font-size:4px;line-height:5px;text-align:center">Lorem Ipsum is simply dummy text of the printing and typesetting industry.</div>
  <div class="abs tiny" style="left:270px;top:130px;width:54px;font-size:4px;line-height:5px;text-align:center">Lorem Ipsum is simply dummy text of the printing and typesetting industry.</div>
  <div class="foot">© 2018 Vantreo. All Rights Reserved.</div><div class="page">10</div>
  <div class="strip"></div>
</section>

<!-- team -->
<section class="slide" style="left:780px;top:2027px;width:341px;height:190px">
  <div class="title">Team Slide</div>
  <div class="subtitle">Lorem ipsum dolor sit amet, consectetur adipiscing elit</div>
  <div class="mini-brand">Vantreo</div>
  <div class="photo" role="img" aria-label="Team member portrait" style="left:25px;top:52px;width:42px;height:43px;background:linear-gradient(135deg,#8a8c8f,#d3d5d8)"></div>
  <div class="photo" role="img" aria-label="Team member portrait" style="left:104px;top:52px;width:42px;height:43px;background:linear-gradient(135deg,#8a8c8f,#d3d5d8)"></div>
  <div class="photo" role="img" aria-label="Team member portrait" style="left:184px;top:52px;width:42px;height:43px;background:linear-gradient(135deg,#8a8c8f,#d3d5d8)"></div>
  <div class="photo" role="img" aria-label="Team member portrait" style="left:264px;top:52px;width:42px;height:43px;background:linear-gradient(135deg,#8a8c8f,#d3d5d8)"></div>
  <div class="badge" style="left:21px;top:103px;width:50px">JANE MORROW</div>
  <div class="badge" style="left:100px;top:103px;width:50px">JANE MORROW</div>
  <div class="badge" style="left:180px;top:103px;width:50px">JANE MORROW</div>
  <div class="badge" style="left:260px;top:103px;width:50px">JANE MORROW</div>
  <div class="role" style="left:21px;top:114px;width:50px">Director</div>
  <div class="role" style="left:100px;top:114px;width:50px">Director</div>
  <div class="role" style="left:180px;top:114px;width:50px">Director</div>
  <div class="role" style="left:260px;top:114px;width:50px">Director</div>
  <div class="abs tiny" style="left:16px;top:126px;width:60px;font-size:4px;line-height:5.5px;text-align:center">Lorem Ipsum is simply dummy text of the printing and typesetting industry</div>
  <div class="abs tiny" style="left:95px;top:126px;width:60px;font-size:4px;line-height:5.5px;text-align:center">Lorem Ipsum is simply dummy text of the printing and typesetting industry</div>
  <div class="abs tiny" style="left:175px;top:126px;width:60px;font-size:4px;line-height:5.5px;text-align:center">Lorem Ipsum is simply dummy text of the printing and typesetting industry</div>
  <div class="abs tiny" style="left:255px;top:126px;width:60px;font-size:4px;line-height:5.5px;text-align:center">Lorem Ipsum is simply dummy text of the printing and typesetting industry</div>
  <div class="foot">© 2018 Vantreo. All Rights Reserved.</div><div class="page">11</div>
  <div class="strip"></div>
</section>

<!-- biography -->
<section class="slide" style="left:71px;top:2236px;width:340px;height:192px">
  <div class="title">Each Member Biography</div>
  <div class="subtitle">Lorem ipsum dolor sit amet, consectetur adipiscing elit</div>
  <div class="mini-brand">Vantreo</div>
  <div class="photo" role="img" aria-label="Team member portrait" style="left:31px;top:51px;width:44px;height:45px;background:linear-gradient(135deg,#8a8c8f,#d3d5d8)"></div>
  <div class="badge" style="left:27px;top:101px;width:50px">JANE MORROW</div>
  <div class="role" style="left:17px;top:112px;width:50px;text-align:left;padding-left:13px">Director</div>
  <div class="abs tiny" style="left:30px;top:122px;width:55px;font-size:4px;line-height:5.5px">Lorem Ipsum is simply dummy text of the printing and typesetting industry</div>
  <div class="abs tiny" style="left:101px;top:52px;width:222px;font-size:4.2px;line-height:7px">Lorem Ipsum is simply dummy text of the printing and typesetting industry. Lorem Ipsum is simply dummy text of the printing and typesetting industry.<br><br>Lorem Ipsum is simply dummy text of the printing and typesetting industry. Lorem Ipsum is simply dummy text of the printing and typesetting industry.<br><br>Lorem Ipsum is simply dummy text of the printing and typesetting industry. Lorem Ipsum is simply dummy text of the printing and typesetting industry.<br><br>Lorem Ipsum is simply dummy text of the printing and typesetting industry. Lorem Ipsum is simply dummy text of the printing and typesetting industry.</div>
  <div class="foot">© 2018 Vantreo. All Rights Reserved.</div><div class="page">12</div>
  <div class="strip"></div>
</section>

<!-- market strategy -->
<section class="slide" style="left:426px;top:2236px;width:340px;height:192px">
  <div class="title">Market Strategy</div>
  <div class="subtitle">Lorem ipsum dolor sit amet, consectetur adipiscing elit</div>
  <div class="mini-brand">Vantreo</div>
  <svg width="170" height="100" style="left:10px;top:42px">
    <rect x="27" y="2" width="116" height="78" rx="2" fill="#3a3b3d"/>
    <rect x="31" y="6" width="108" height="66" fill="#fff"/>
    <g stroke="#e1e2e4" stroke-width="0.5"><path d="M31 20h108M31 34h108M31 48h108M31 62h108M49 6v66M67 6v66M85 6v66M103 6v66M121 6v66"/></g>
    <path d="M31 48l18-10 18 8 18-20 18 12 18-16 18 6v44H31z" fill="var(--magenta)" opacity=".85"/>
    <path d="M31 58l18-6 18 4 18-12 18 8 18-10 18 4v26H31z" fill="var(--green)" opacity=".85"/>
    <path d="M31 62l18-2 18 3 18-6 18 4 18-4 18 2v13H31z" fill="var(--blue)" opacity=".85"/>
    <path d="M80 80h10l3 10H77z" fill="#c4c6c9"/><rect x="66" y="90" width="38" height="3" fill="#aeb0b3"/>
    <path d="M143 12h12M27 30h-5" stroke="var(--ink)" stroke-width="0.6"/><path d="M143 32h8" stroke="var(--ink)" stroke-width="0.6"/>
  </svg>
  <div class="abs" style="left:8px;top:67px;font-size:8px">67%</div>
  <div class="abs" style="left:168px;top:49px;font-size:8px">93%</div>
  <div class="abs" style="left:163px;top:70px;font-size:8px">41%</div>
  <svg width="8" height="60" style="left:200px;top:52px" fill="none" stroke="var(--blue)" stroke-width="0.8"><circle cx="4" cy="3" r="2.2"/><circle cx="4" cy="17" r="2.2"/><circle cx="4" cy="31" r="2.2"/><circle cx="4" cy="45" r="2.2"/></svg>
  <div class="abs tiny" style="left:211px;top:50px;width:116px;font-size:4px;line-height:4.7px">Lorem Ipsum is simply dummy text of the printing and typesetting industry<br>Lorem Ipsum is simply dummy text of the printing and typesetting industry<br>Lorem Ipsum is simply dummy text of the printing and typesetting industry<br>Lorem Ipsum is simply dummy text of the printing and typesetting industry</div>
  <div class="abs tiny" style="left:17px;top:152px;width:310px;font-size:4px;line-height:5.5px">Lorem Ipsum is simply dummy text of the printing and typesetting industry. Lorem Ipsum is simply dummy text of the printing and typesetting industry. Lorem Ipsum is simply dummy text of the printing and typesetting industry. Lorem Ipsum is simply dummy text of the printing and typesetting industry. Lorem Ipsum is simply dummy text of the printing.</div>
  <div class="foot">© 2018 Vantreo. All Rights Reserved.</div><div class="page">13</div>
  <div class="strip"></div>
</section>

<!-- tea break -->
<section class="slide" style="left:780px;top:2236px;width:341px;height:192px;background:var(--blue)">
  <div class="photo" role="img" aria-label="Faint coffee cup and phone on a desk" style="left:0;top:0;width:341px;height:192px;background:linear-gradient(135deg,#2a8fd6 0%,#3b9ade 45%,#2383c7 100%)"></div>
  <div class="abs" style="left:36px;top:76px;font-size:24px;letter-spacing:.5px;color:var(--white)">TEA BREAK</div>
  <div class="abs wordmark" style="left:216px;top:92px;font-size:24px;color:var(--white)">Vantreo</div>
</section>

<!-- percent graphics -->
<section class="slide" style="left:71px;top:2450px;width:340px;height:190px">
  <div class="title">Percent Graphics</div>
  <div class="subtitle">Lorem ipsum dolor sit amet, consectetur adipiscing elit</div>
  <div class="mini-brand">Vantreo</div>
  <svg width="340" height="60" style="left:0;top:45px" fill="none" stroke-width="5">
    <circle cx="51" cy="25" r="20" stroke="#d6d7d9"/><circle cx="51" cy="25" r="20" stroke="var(--blue)" stroke-dasharray="78 126" transform="rotate(-90 51 25)"/>
    <circle cx="164" cy="25" r="20" stroke="#d6d7d9"/><circle cx="164" cy="25" r="20" stroke="var(--green)" stroke-dasharray="63 126" transform="rotate(-90 164 25)"/>
    <circle cx="275" cy="25" r="20" stroke="#d6d7d9"/><circle cx="275" cy="25" r="20" stroke="var(--magenta)" stroke-dasharray="47 126" transform="rotate(-90 275 25)"/>
    <g stroke-width="1"><circle cx="51" cy="25" r="6" stroke="var(--blue)"/><rect x="159" y="20" width="10" height="10" stroke="var(--green)"/><rect x="270" y="20" width="10" height="9" stroke="var(--magenta)"/></g>
  </svg>
  <div class="abs" style="left:30px;top:103px;width:42px;text-align:center;font-size:15px;color:var(--blue)">62<span style="font-size:9px">%</span></div>
  <div class="abs" style="left:143px;top:103px;width:42px;text-align:center;font-size:15px;color:var(--green)">50<span style="font-size:9px">%</span></div>
  <div class="abs" style="left:254px;top:103px;width:42px;text-align:center;font-size:15px;color:var(--magenta)">37<span style="font-size:9px">%</span></div>
  <div class="abs" style="left:16px;top:125px;width:70px;text-align:center;font-size:5px;color:var(--blue)">LOREM IPSUM</div>
  <div class="abs" style="left:129px;top:125px;width:70px;text-align:center;font-size:5px;color:var(--green)">LOREM IPSUM</div>
  <div class="abs" style="left:240px;top:125px;width:70px;text-align:center;font-size:5px;color:var(--magenta)">LOREM IPSUM</div>
  <div class="abs tiny" style="left:11px;top:134px;width:80px;font-size:4px;line-height:5px;text-align:center">Lorem Ipsum is simply dummy text of the printing and typesetting industry. Lorem Ipsum is simply dummy text of the printing and typesetting industry.</div>
  <div class="abs tiny" style="left:124px;top:134px;width:80px;font-size:4px;line-height:5px;text-align:center">Lorem Ipsum is simply dummy text of the printing and typesetting industry. Lorem Ipsum is simply dummy text of the printing and typesetting industry.</div>
  <div class="abs tiny" style="left:235px;top:134px;width:80px;font-size:4px;line-height:5px;text-align:center">Lorem Ipsum is simply dummy text of the printing and typesetting industry. Lorem Ipsum is simply dummy text of the printing and typesetting industry.</div>
  <div class="strip"></div>
</section>

<!-- demographic -->
<section class="slide" style="left:71px;top:2650px;width:340px;height:191px">
  <div class="title">Demographic Statistic</div>
  <div class="subtitle">Lorem ipsum dolor sit amet, consectetur adipiscing elit</div>
  <div class="mini-brand">Vantreo</div>
  <svg width="340" height="150" style="left:0;top:38px" fill="none" stroke-width="0.8">
    <g stroke="var(--violet)"><rect x="50" y="6" width="32" height="14"/><path d="M66 20v5"/><rect x="108" y="6" width="32" height="14"/><path d="M124 20v5"/></g>
    <g stroke="var(--green)"><rect x="220" y="6" width="32" height="14"/><path d="M236 20v5"/></g>
    <g stroke="var(--blue)"><rect x="289" y="6" width="32" height="14"/><path d="M305 20v5"/></g>
    <path d="M20 26h150" stroke="var(--violet)" stroke-width="1.5"/><path d="M180 26h150" stroke="var(--green)" stroke-width="1.5"/>
    <g stroke="var(--green)"><rect x="30" y="89" width="32" height="14"/><path d="M46 103v5"/><rect x="90" y="89" width="32" height="14"/><path d="M106 103v5"/></g>
    <g stroke="var(--magenta)"><rect x="183" y="89" width="32" height="14"/><path d="M199 103v5"/></g>
    <g stroke="var(--violet)"><rect x="241" y="89" width="32" height="14"/><path d="M257 103v5"/></g>
    <path d="M20 109h150" stroke="var(--green)" stroke-width="1.5"/><path d="M180 109h150" stroke="var(--violet)" stroke-width="1.5"/>
  </svg>
  <div class="abs tiny" style="left:30px;top:73px;width:125px;font-size:4px;line-height:5px;text-align:center">Lorem Ipsum is simply dummy text of the printing and typesetting industry.</div>
  <div class="abs tiny" style="left:190px;top:73px;width:125px;font-size:4px;line-height:5px;text-align:center">Lorem Ipsum is simply dummy text of the printing and typesetting industry.</div>
  <div class="abs tiny" style="left:30px;top:156px;width:125px;font-size:4px;line-height:5px;text-align:center">Lorem Ipsum is simply dummy text of the printing and typesetting industry.</div>
  <div class="abs tiny" style="left:190px;top:156px;width:125px;font-size:4px;line-height:5px;text-align:center">Lorem Ipsum is simply dummy text of the printing and typesetting industry.</div>
  <div class="foot">© 2018 Vantreo. All Rights Reserved.</div><div class="page">15</div>
  <div class="strip"></div>
</section>

<!-- thank you -->
<section class="slide" style="left:426px;top:2450px;width:695px;height:391px">
  <div class="photo" role="img" aria-label="Faded server room with two engineers" style="left:0;top:0;width:695px;height:391px;background:var(--photo-light)"></div>
  <div class="abs wordmark" style="left:63px;top:232px;font-size:58px">Vantreo</div>
  <div class="abs headline" style="left:365px;top:96px;font-size:30px;line-height:40px">Thank you<br>for your time!</div>
  <div class="abs" style="left:365px;top:193px;font-size:13.5px;line-height:19px;color:var(--ink)">48 Linden Row, Marlow Bay,<br>suite 880, Avendale</div>
  <svg width="14" height="60" style="left:366px;top:244px" fill="none" stroke="var(--blue)" stroke-width="1.2">
    <path d="M2 3c1-1 3-1 4 0l1 2-2 1c0 2 2 4 4 4l1-2 2 1c1 1 1 3 0 4-5 1-11-5-10-10z" fill="var(--blue)" stroke="none"/>
    <path d="M2 24c1-1 3-1 4 0l1 2-2 1c0 2 2 4 4 4l1-2 2 1c1 1 1 3 0 4-5 1-11-5-10-10z" fill="var(--blue)" stroke="none"/>
    <rect x="1" y="44" width="12" height="9"/><path d="M1 44l6 5 6-5"/>
  </svg>
  <div class="abs" style="left:388px;top:240px;font-size:13.5px;line-height:21px;color:var(--ink)">555-014-2290<br>555-014-2291<br>name@vantreo.info</div>
  <div class="foot" style="left:22px;bottom:10px;font-size:7px">© 2018 Vantreo. All Rights Reserved.</div>
  <div class="page" style="right:22px;bottom:10px;font-size:7px">01</div>
  <div class="strip" style="height:5px"></div>
</section>

</body>
</html>
```